New Architectural Firm Business Cards

New Business card to compliment previous pixel forum logo (attached). Please design a business card that is simple, modern, creative....please do not use "symbols", simply the logo and associated graphics/text. The front should contain name/address/phone/email/web address (with graphics).....back should be 100% graphic design using the logo somehow. Hoping for a two color (black and yellow) design. full bleed design, no borders

Target Market(s)

Commercial Architecture Clients

Industry/Entity Type

Architecture

Contact Information for Business Card

Please design a business card that is simple, modern, creative....please do not use "symbols", simply the logo and associated graphics/text. The front should contain name/address/phone/email/web address (with graphics).....back should be 100% graphic design using the logo somehow

Font styles to use
Sans Serif

Colors
FFF300
FFF600
FEFA6F
FFFEC7
FFFEE8

Requirements
Must have
• Clean, Modern Design
Should not have
• Stock images or "icons"

```html
<!DOCTYPE html>
<html lang="en">
<head>
<meta charset="utf-8">
<title>Norvale Architecture – Business Cards</title>
<link rel="stylesheet" href="https://fonts.googleapis.com/css2?family=Montserrat:wght@400;600;700&display=swap">
<style>
  :root {
    --yellow: #F6C413;
    --ink: #231F20;
    --text: #3b3b3b;
    --paper: #ffffff;
    --page: #ffffff;
  }
  * { box-sizing: border-box; margin: 0; padding: 0; }
  html, body {
    width: 687px; height: 1200px; overflow: hidden;
    background: var(--page);
    font-family: "Montserrat", sans-serif;
  }
  .sheet {
    width: 687px; height: 1200px;
    display: flex; flex-direction: column; align-items: center; justify-content: center;
    gap: 40px;
  }
  .card {
    position: relative;
    width: 600px; height: 343px;
    background: var(--paper);
    overflow: hidden;
    box-shadow: 0 1px 6px rgba(0,0,0,0.22);
  }
  .bar { position: absolute; }
  .bar--yellow { background: var(--yellow); }
  .bar--black { background: var(--ink); }

  .wordmark {
    position: absolute;
    color: var(--yellow);
    font-weight: 700;
    text-transform: uppercase;
    line-height: 1;
    text-align: center;
  }
  .wordmark__name { display: block; font-size: 46px; letter-spacing: 1px; }
  .wordmark__line { display: block; font-size: 21.5px; letter-spacing: 0.5px; margin-top: 8px; }

  .front .wordmark { left: 62px; top: 140px; width: 200px; }
  .back .wordmark { left: 194px; top: 128px; width: 212px; }

  .contact { position: absolute; left: 312px; top: 72px; color: var(--text); }
  .contact__name {
    color: var(--yellow); font-weight: 600; font-size: 21.5px;
    letter-spacing: 0.2px; line-height: 1;
  }
  .contact__role {
    color: var(--ink); font-weight: 700; font-size: 13px;
    letter-spacing: 0.3px; margin-top: 5px;
  }
  .contact__details { list-style: none; margin-top: 22px; font-size: 15px; }
  .contact__details li { line-height: 1.3; margin-bottom: 11px; }
  .contact__web strong { font-weight: 700; }
</style>
</head>
<body>
<main class="sheet">

  <section class="card front" aria-label="Card front">
    <div class="bar bar--yellow" style="left:313px; top:0; width:26px; height:62px;"></div>
    <div class="bar bar--black" style="left:0; bottom:0; width:260px; height:27px;"></div>

    <div class="wordmark">
      <span class="wordmark__name">Norvale</span>
      <span class="wordmark__line">Architecture</span>
    </div>

    <div class="contact">
      <p class="contact__name">MARCO VELDEN</p>
      <p class="contact__role">DESIGN PRINCIPAL</p>
      <ul class="contact__details">
        <li>PO Box 512, Larch Lane,<br>NSW, 2190, FL 410200</li>
        <li>(000) 555 0173</li>
        <li>info@norvalestudio.com</li>
        <li class="contact__web">www.<strong>norvalestudio</strong>.com</li>
      </ul>
    </div>
  </section>

  <section class="card back" aria-label="Card back">
    <div class="bar bar--yellow" style="left:0; top:0; width:26px; height:62px;"></div>
    <div class="bar bar--black" style="right:0; top:0; width:260px; height:26px;"></div>
    <div class="bar bar--yellow" style="right:0; bottom:0; width:26px; height:63px;"></div>
    <div class="bar bar--black" style="left:0; bottom:0; width:260px; height:27px;"></div>

    <div class="wordmark">
      <span class="wordmark__name">Norvale</span>
      <span class="wordmark__line">Architecture</span>
    </div>
  </section>

</main>
</body>
</html>
```